Stonebrook 720 Real Estate Investment Company

We need a business card designed for a real estate investment company named Stonebrook 720. We want to use red#f04a50, orange #f37122 and yellow #fbee3e as the color scheme. The logo colors will need to be modified from the current blue palette. I've attach VitaPathway logo example that captures the color scheme we're going for for Stonebrook 720. Looking for clean Sans Serif fonts.
Contact Information for Business Card
Daniel Furlow
Managing Partner
48317 Whitfield Lane, Suite 510
Tampa, FL 33718
813-555-4870 Mobile
dfurlow@stonebrook720.example
www.stonebrook720.example
Requirements
Must have
- Looking for creative responses.
Nice to have
- Must hit color palette... orange, red, yellow

```html
<!DOCTYPE html>
<html lang="en">
<head>
<meta charset="utf-8">
<title>Stonebrook720 Business Card</title>
<link rel="stylesheet" href="https://fonts.googleapis.com/css2?family=Oswald:wght@700&family=Arimo:wght@400&family=Source+Sans+3:wght@400;600&display=swap">
<style>
  :root {
    --backdrop: #333333;
    --paper: #ffffff;
    --ink: #000000;
    --orange: #ff6633;
    --red: #ff3333;
    --yellow: #ffff33;
    --brand-orange: #f37122;
  }
  * { margin: 0; padding: 0; box-sizing: border-box; }
  html, body {
    width: 1200px; height: 1200px; overflow: hidden;
    background: var(--backdrop);
  }
  .canvas { position: relative; width: 1200px; height: 1200px; }
  .card {
    position: absolute; background: var(--paper); overflow: hidden;
  }
  .card--front { left: 116px; top: 35px; width: 973px; height: 557px; }
  .card--back { left: 114px; top: 616px; width: 973px; height: 556px; }
  .stripes { position: absolute; inset: 0; width: 100%; height: 100%; }
  .stripe--orange { fill: var(--orange); }
  .stripe--red { fill: var(--red); }
  .stripe--yellow { fill: var(--yellow); }

  .wordmark {
    position: absolute; display: flex; align-items: center;
    font-family: "Oswald", sans-serif; font-weight: 700; color: var(--ink);
    line-height: 1; letter-spacing: -0.5px;
  }
  .wordmark__dot { border-radius: 50%; background: var(--brand-orange); }
  .card--front .wordmark { left: 152px; top: 178px; font-size: 74px; gap: 26px; }
  .card--front .wordmark__dot { width: 56px; height: 56px; }
  .card--back .wordmark { left: 513px; top: 383px; font-size: 50px; gap: 18px; }
  .card--back .wordmark__dot { width: 38px; height: 38px; }

  .contact {
    position: absolute; left: 511px; top: 332px;
    font-family: "Arimo", sans-serif; color: var(--ink); line-height: 1;
  }
  .contact__name { font-size: 52px; letter-spacing: -0.3px; }
  .contact__title { font-size: 38px; margin-top: 10px; }
  .contact__phone { font-size: 32px; margin-top: 8px; }
  .contact__email { font-size: 28px; margin-top: 10px; }

  .company {
    position: absolute; left: 0; width: 986px; top: 170px;
    text-align: center; font-family: "Source Sans 3", sans-serif;
    color: var(--ink); line-height: 1;
  }
  .company__name { font-size: 58px; font-weight: 600; }
  .company__line { font-size: 40px; font-weight: 400; margin-top: 8px; }
</style>
</head>
<body>
<main class="canvas">
  <section class="card card--front">
    <svg class="stripes" viewBox="0 0 1568 897" preserveAspectRatio="none" aria-hidden="true">
      <polygon class="stripe--orange" points="1568,8 1319,893 1568,893"/>
      <polygon class="stripe--red" points="1568,465 1319,893 1568,893"/>
      <polygon class="stripe--yellow" points="1568,677 1319,893 1568,893"/>
    </svg>
    <div class="wordmark">Stonebrook720<span class="wordmark__dot"></span></div>
    <div class="contact">
      <p class="contact__name">Daniel Furlow</p>
      <p class="contact__title">Managing Partner</p>
      <p class="contact__phone">813-555-4870 Mobile</p>
      <p class="contact__email">dfurlow@stonebrook720.example</p>
    </div>
  </section>

  <section class="card card--back">
    <svg class="stripes" viewBox="0 0 1566 896" preserveAspectRatio="none" aria-hidden="true">
      <polygon class="stripe--orange" points="0,13 248,893 0,893"/>
      <polygon class="stripe--red" points="0,462 248,893 0,893"/>
      <polygon class="stripe--yellow" points="0,673 248,893 0,893"/>
    </svg>
    <div class="company">
      <p class="company__name">Stonebrook720</p>
      <p class="company__line">48317 Whitfield Lane, Suite 510</p>
      <p class="company__line">Tampa, FL 33718</p>
      <p class="company__line">www.stonebrook720.example</p>
    </div>
    <div class="wordmark">Stonebrook720<span class="wordmark__dot"></span></div>
  </section>
</main>
</body>
</html>
```